Dynamic Website Design For Dynamic Speaker and Business Coach!

Professional Website Design for a for a Professional Business coach, Business trainer, and Speaker.

Note: This is for design only. No coding required. We want to see your ideas for a great website! This will be a FUN design and not boring like others you may work on.

Please let your creative ideas flow. We have given you a ton of info along with videos to help you understand what we are after, however we WANT your creativity to shine through in your designs!

We are a professional company that has run hundreds of crowdsourced projects on multiple platforms. If you participate in this contest (we hope you do) you can expect great video feedback, consistent feedback, and also our guarantee that if we know your website design will not be what we are looking for we will notify you so you don’t waste your time if there is no chance of you winning.

We respect and recognize this is how you make your living and we will not play games. We look forward to an awesome contest and awesome website designs.

Design Brief:

We are looking for a fresh and fun new design for

http://www.brightpath-advisory.net

This individual (Dana Holloway) teaches and trains corporations and businesses in the fields of leadership, sales, communication, business operations etc. Additionally this business teaches and mentors business professionals in a small group level or 1 on 1.

The website needs to convey trust, professionalism, and affluent, while at the same time having some personality!

This business operates on 3 core principles that we would like to see incorporated into the logo if it is a good fit. The 3 principals are:

Focus
Accountability
Results

Here is a video to help explain what we like about the current site and what we don’t like:
http://clipvault.example/t/QwpLmr82kTnb

As you can see the website is geared towards business professionals. Please look over the website to learn what they do. Obviously this is not a good website so we need your help.

We want a website that is professional-looking, has personality and is geared more towards promoting Dana Holloway, the owner of Summit Path Advisory as a Speaker and Business Consultant. The more you can incorporate clean, professional and fun personality elements into the design, the better off you are at winning.

Here are some examples of other sites in their business that have some things we like:

http://velvetcompass.com Please watch video to learn what we like and don’t like:
http://clipvault.example/t/NrtHq7YpLwc

http://tallpinegrowth.com Please watch video to learn what we like and don’t like:
http://clipvault.example/t/J8vDkrWa

http://www.marthaquince.com Please watch video to learn what we like and don’t like:
http://clipvault.example/t/Pz3mx9Rb2Kq

http://www.vantix7.com Please watch video to learn what we like and don’t like:
http://clipvault.example/t/7Gwe4sNhydv

NOTE: We do not want to copy anything outright. We want to learn, model and take their ideas and make them better. We also want to be flexible and take what we like along with your creativity to make an amazing design.

Here is what we are looking for in more specific terms:

Colors: We like the darker blue (not the light blue like the site) and also a burnt orange. I’ve attached her Logo so you can get an idea and feel for the colors.

When looking at colors please know that the current site and look is NOT what we are going for. We are going for a clean and professional look but also a look that is BOLD, FUN, and Vibrant (hence the colors).

Menu: Horizontal. We like bold and easy to read menu items. Don’t make it small and cluttered.

Site Structure: Clean and easy to navigate. We have a lot of content to display so we need a clean structure that breaks up the text and content areas.
Images: Please pull images from the current site. We can always replace the images of course, but if you show them “their own stuff” in the new design you will be closer to winning because it will feel more like “them”

Look and Feel: Professional. Fun. High-End. Business-like. This website needs to convey that Dana Holloway and Summit Path Advisory are professional. That Dana Holloway is a sought-after Speaker and Business Consultant who knows what she is talking about; can be serious when she needs to be, but also likes to have fun with her clients. This site must convey that!

Content Areas: It is a safe bet that if it is on the current site we need it on the new site. So don’t drop anything as it makes it hard to “cut content”.

What we don't want: We do not want clutter, boring, or templates or themes. We don’t want too cartoony, too cute, or too fancy… Be creative!

Out of respect to professional designers who really are working hard to win if you do not follow this brief, you submit worn out themes, templates, or boring designs you will be eliminated. We are offering great prize money for this so we expect great visual designs.
Updates

Project Deadline Extended
Reason: Our client is out of town, and waiting to hear feedback from them. So, in the meantime, we wanted to keep the project going to see what else you designers can come up with. As soon as we hear back from our client, we will pass along the info. Thanks!

Target Market(s)

Target Audience is entrepreneurs and business professionals alike. This is all business to business stuff.

This person teaches and trains startups and billion dollar companies. The common thread is that they are all businesses and companies who need help in various areas including sales, communication, business operations, etc.

Industry/Entity Type

Business

Font styles to use
Sans Serif

Requirements
Must have
• Brief is very detailed. Please review
Nice to have
Should not have

```html
<!DOCTYPE html>
<html lang="en">
<head>
<meta charset="utf-8">
<title>Summit Path Advisory</title>
<link href="https://fonts.googleapis.com/css2?family=Open+Sans:wght@400;600;700;800&family=Open+Sans+Condensed:wght@300&display=swap" rel="stylesheet">
<style>
:root{
  --navy:#0b3a8c;
  --navy-dark:#0a2f6e;
  --orange:#f06a0f;
  --text:#777;
  --heading:#1c2f6b;
  --light:#f3f3f3;
  --footer:#3b3b3b;
  --line:#dcdcdc;
}
*{margin:0;padding:0;box-sizing:border-box}
html,body{width:724px;height:1200px;overflow:hidden;background:#fff}
body{font-family:"Open Sans",Arial,sans-serif;color:var(--text);position:relative}
.abs{position:absolute}

.topline{left:0;top:0;width:724px;height:2px;background:var(--navy-dark)}
.brand{left:80px;top:22px;display:flex;align-items:center;gap:8px}
.brand-dot{width:24px;height:24px;border-radius:50%;background:var(--orange)}
.brand-name{font-size:17px;font-weight:700;color:var(--navy)}
.call{right:78px;top:28px;font-size:11.5px;font-weight:700;color:#333;display:flex;align-items:center;gap:6px}
.call b{color:var(--orange)}

.nav{left:0;top:70px;width:724px;height:32px;background:var(--navy);display:flex;padding-left:80px}
.nav span{color:#fff;font-size:7.4px;font-weight:600;line-height:32px;padding:0 9px;border-right:1px solid rgba(255,255,255,.15)}
.nav span:first-child{padding-left:12px}

.hero{left:0;top:102px;width:724px;height:309px;background:linear-gradient(180deg,#b9bfca 0%,#9ea6b6 45%,#7d869a 100%)}
.hero-rule{left:171px;width:380px;height:1px;background:rgba(255,255,255,.8)}
.hero-title{left:0;width:724px;top:208px;text-align:center;font-size:38px;font-weight:800;color:#fff;letter-spacing:.5px}
.hero-title em{font-style:normal;color:var(--navy)}
.hero-sub{left:140px;width:444px;top:270px;text-align:center;font-family:Arial,sans-serif;font-size:6.7px;line-height:14px;color:#fff}
.search{left:149px;top:311px;width:428px;height:35px;background:rgba(90,95,105,.55);padding:5px}
.search-field{position:absolute;left:5px;top:5px;width:370px;height:25px;background:rgba(255,255,255,.25);color:#fff;font-size:7.6px;line-height:25px;padding-left:10px}
.search-btn{position:absolute;right:5px;top:5px;width:52px;height:25px;background:var(--orange);color:#fff;font-size:8px;text-align:center;line-height:25px}
.arrow{top:359px;width:22px;height:22px;border-radius:50%;background:rgba(60,60,60,.6)}

.welcome-title{left:80px;top:425px;font-size:16px;font-weight:700;color:var(--heading)}
.welcome-title em{font-style:normal;color:var(--orange)}
.p{font-family:Arial,sans-serif;font-size:6.6px;line-height:14px;color:var(--text)}
.btn{background:var(--orange);color:#fff;font-size:8px;text-align:center}
.signup{left:462px;top:423px;width:183px;height:156px;background:#f6f6f6;border:1px solid var(--line)}
.signup .k{position:absolute;left:0;width:100%;text-align:center;color:#333}
.field{position:absolute;left:12px;width:163px;height:21px;background:#fff;border:1px solid var(--line);font-size:6px;line-height:19px;padding-left:8px;color:#aaa}

.video-band{left:0;top:587px;width:724px;height:215px;background:linear-gradient(90deg,#e6e9ef,#f3f4f7 50%,#e9ebf0)}
.video-title{left:89px;top:607px;font-size:18px;color:#555;font-weight:400}
.video-lead{left:90px;top:633px;width:230px;font-size:8px;line-height:13px;color:var(--orange)}
.video{left:340px;top:603px;width:299px;height:179px;background:linear-gradient(135deg,#3f7fb8,#2a5f96)}
.vbar{left:340px;top:759px;width:299px;height:23px;background:rgba(10,25,45,.75)}

.h3{font-size:12px;font-weight:700;color:var(--heading)}
.news-date{width:28px;text-align:center;font-size:8px;color:#555;border-right:2px solid var(--line)}
.news-date b{display:block;color:var(--orange);font-size:9px}
.news-head{font-size:7.8px;color:var(--orange)}
.divider{height:1px;background:var(--line)}
.photo{width:67px;height:59px;background:linear-gradient(180deg,#c9ccd2,#8c929c)}
.t-name{font-size:8.6px;color:var(--orange)}
.t-date{font-size:6.4px;font-style:italic;color:#222}
.quote{font-size:14px;color:#555;font-weight:700}

.footer{left:0;top:1098px;width:724px;height:102px;background:var(--footer)}
.badge{top:1114px;width:34px;height:34px;border-radius:50%;background:#6b7da1}
.newsletter{left:239px;top:1120px;font-family:"Open Sans Condensed",sans-serif;font-size:14px;color:#aaa}
.nl-text{left:319px;top:1120px;font-size:5.7px;line-height:12px;color:#aaa}
.nl-field{left:483px;top:1121px;width:151px;height:24px;background:#eee;border:1px solid #999;font-size:5.4px;line-height:22px;padding-left:24px;color:#777}
.foot-rule{left:87px;top:1160px;width:560px;height:1px;background:#555}
.copy{left:80px;top:1175px;font-family:Arial,sans-serif;font-size:6.6px;color:#ddd}
.social{top:1167px;width:20px;height:20px;border-radius:50%;border:1px solid #999}
</style>
</head>
<body>
<div class="abs topline"></div>
<div class="abs brand"><span class="brand-dot"></span><span class="brand-name">Summit Path Advisory</span></div>
<div class="abs call">
  <svg width="16" height="12" viewBox="0 0 16 12"><path d="M1 4 Q8 -1 15 4 L13 6 L11 4 L5 4 L3 6 Z" fill="#333"/><rect x="3" y="6" width="10" height="6" rx="1" fill="#333"/></svg>
  CALL US : <b>(555)-214-7730</b>
</div>

<nav class="abs nav">
  <span>HOME</span><span>PASSION</span><span>WHO WE ARE</span><span>SPEAKER</span><span>FREE VIDEOS</span><span>WEB TV SHOW</span><span>TESTIMONIALS</span><span>LINDELL LEARNING</span><span>BLOG</span><span>CONTACT</span>
</nav>

<section class="abs hero" role="img" aria-label="Photo of a smiling business team giving thumbs up"></section>
<div class="abs hero-rule" style="top:204px"></div>
<h1 class="abs hero-title">SUMMIT PATH <em>ADVISORY</em></h1>
<div class="abs hero-rule" style="top:260px"></div>
<p class="abs hero-sub">Are you searching to bridge the gap between where you are and where you want to be? As you face greater pressure to "move the needle" on your company's productivity and bottom line profitability, how prepared are you to step in and shine as the leader</p>
<div class="abs search"><div class="search-field">Enter any keyword............</div><div class="search-btn">SEARCH</div></div>
<svg class="abs arrow" style="left:337px" viewBox="0 0 22 22"><path d="M13 6 L8 11 L13 16" stroke="#fff" stroke-width="2" fill="none"/></svg>
<svg class="abs arrow" style="left:365px" viewBox="0 0 22 22"><path d="M9 6 L14 11 L9 16" stroke="#fff" stroke-width="2" fill="none"/></svg>

<h2 class="abs welcome-title">Welcome TO <em>Summit Path</em> Advisory</h2>
<p class="abs p" style="left:80px;top:454px;width:355px">Dana Holloway is a results-based professional with over 25 years of experience in sales, marketing, facilitation, training and coaching. Committed to delivering more than expected by customers and clients. In 2008, opportunity knocked and she founded Summit Path Advisory.</p>
<p class="abs p" style="left:80px;top:505px;width:360px">Together we'll explore where YOU are and where YOU want to go. By building a solid vision as the leader, and communicating it clearly, you're committing to greater results and expecting your employees to ramp up their game as well. At ute with more of a sense of ownership on the job.....</p>
<div class="abs btn" style="left:79px;top:556px;width:70px;height:19px;line-height:19px">READ MORE</div>

<aside class="abs signup">
  <div class="k" style="top:16px;font-size:6.4px">CHANGE YOUR THINKING, CHANGE YOUR RESULTS!</div>
  <div class="k" style="top:28px;font-size:8.4px">SIGN UP FOR MY FREE REPORT</div>
  <div class="field" style="top:51px">Enter Your email Id :</div>
  <div class="field" style="top:86px">Enter Your Password :</div>
  <div class="btn" style="position:absolute;left:50px;top:121px;width:84px;height:20px;line-height:20px">SUBSCRIBE</div>
</aside>

<section class="abs video-band" role="img" aria-label="Faint background photo of smiling people"></section>
<h2 class="abs video-title">OUR VIDEO</h2>
<p class="abs video-lead">As you face greater pressure to "move the needle" on your company's productivity</p>
<p class="abs p" style="left:91px;top:670px;width:235px;font-size:6.4px;line-height:13px;color:#999">Dana Holloway is a results-based professional with over 25 years of experience in sales, marketing, facilitation, training and coaching. Committed to deliverknocked and she founded Summit Path Advisory.</p>
<p class="abs p" style="left:91px;top:721px;width:235px;font-size:6.4px;line-height:13px;color:#999">Dana Holloway is a results-based professional with over 25 years of experience in sales, marketing, facilitation, training and coaching. Committed to deliverknocked and she founded Summit Path Advisory.</p>
<div class="abs video" role="img" aria-label="Video still of the speaker presenting beside a headline about focus, accountability and results"></div>
<div class="abs vbar"></div>
<svg class="abs" style="left:340px;top:759px" width="299" height="23" viewBox="0 0 299 23">
  <rect width="32" height="23" fill="#111"/><path d="M12 6 L21 11.5 L12 17 Z" fill="#fff"/>
  <rect x="38" y="10" width="222" height="3" fill="#2b3f55"/>
  <rect x="266" y="7" width="2" height="9" fill="#5fb4e8"/><rect x="270" y="7" width="2" height="9" fill="#5fb4e8"/><rect x="274" y="7" width="2" height="9" fill="#5fb4e8"/>
</svg>

<h3 class="abs h3" style="left:79px;top:820px">LATEST NEWS</h3>
<div class="abs news-date" style="left:80px;top:851px;height:26px"><b>22</b>JUN</div>
<div class="abs news-head" style="left:118px;top:853px">NEQUE PORRO QUISQUAM EST QUI DOLOREM</div>
<p class="abs p" style="left:118px;top:866px;width:240px;font-size:6.4px;line-height:13px">Donec viverra auctor lobortis. Pellentesque eu est a nulla placerat dignissim. Morbi a enim in magna semper bibendum. Etiam scelerisque, nunc ac egestas consequat, odio nibh euismod nulla, eget auctor orci nibh vel nisi.</p>
<div class="abs divider" style="left:79px;top:920px;width:275px"></div>
<div class="abs news-date" style="left:80px;top:934px;height:26px"><b>22</b>JUN</div>
<div class="abs news-head" style="left:118px;top:936px">NEQUE PORRO QUISQUAM EST QUI DOLOREM</div>
<p class="abs p" style="left:118px;top:949px;width:240px;font-size:6.4px;line-height:13px">Donec viverra auctor lobortis. Pellentesque eu est a nulla placerat dignissim. Morbi a enim in magna semper bibendum. Etiam scelerisque, nunc ac egestas consequat, odio nibh euismod nulla, eget auctor orci nibh vel nisi.</p>
<div class="abs divider" style="left:79px;top:1003px;width:275px"></div>
<div class="abs news-date" style="left:80px;top:1021px;height:26px"><b>22</b>JUN</div>
<div class="abs news-head" style="left:118px;top:1023px">NEQUE PORRO QUISQUAM EST QUI DOLOREM</div>
<p class="abs p" style="left:118px;top:1036px;width:240px;font-size:6.4px;line-height:13px">Donec viverra auctor lobortis. Pellentesque eu est a nulla placerat dignissim. Morbi a enim in magna semper bibendum. Etiam scelerisque, nunc ac egestas consequat, odio nibh euismod nulla, eget auctor orci nibh vel nisi.</p>

<h3 class="abs h3" style="left:372px;top:820px">OUR TESTIMONIALS</h3>
<svg class="abs" style="left:619px;top:823px" width="26" height="11" viewBox="0 0 26 11"><rect width="11" height="11" fill="#bbb"/><rect x="14" width="11" height="11" fill="#bbb"/><path d="M7 3 L4 5.5 L7 8" stroke="#fff" fill="none"/><path d="M18 3 L21 5.5 L18 8" stroke="#fff" fill="none"/></svg>
<div class="abs photo" style="left:372px;top:855px" role="img" aria-label="Portrait of a male client"></div>
<div class="abs t-name" style="left:456px;top:853px">MARCUS DOYLE</div>
<div class="abs t-date" style="left:456px;top:866px">on posed 22 june 2014</div>
<div class="abs quote" style="left:443px;top:873px">“</div>
<p class="abs p" style="left:457px;top:881px;width:190px;font-size:6.4px;line-height:13px">Donec viverra auctor lobortis. Pellentesque eu est a nulla placerat dignissim. Morbi a enim in magna semper bibendum. Etiam scelerisque, nunc ac egestas consequat, odio nibh euismod nulla, eget auctor orci nibh vel nisi placerat dignissim. Morbi a enim in magna semper bibendum....</p>
<div class="abs quote" style="left:549px;top:935px">”</div>
<div class="abs divider" style="left:372px;top:963px;width:273px"></div>
<div class="abs photo" style="left:372px;top:981px" role="img" aria-label="Portrait of a female client"></div>
<div class="abs t-name" style="left:456px;top:979px">MARCUS DOYLE</div>
<div class="abs t-date" style="left:456px;top:992px">on posed 22 june 2014</div>
<div class="abs quote" style="left:443px;top:999px">“</div>
<p class="abs p" style="left:457px;top:1007px;width:190px;font-size:6.4px;line-height:13px">Donec viverra auctor lobortis. Pellentesque eu est a nulla placerat dignissim. Morbi a enim in magna semper bibendum. Etiam scelerisque, nunc ac egestas consequat, odio nibh euismod nulla, eget auctor orci nibh vel nisi placerat dignissim. Morbi a enim in magna semper bibendum....</p>
<div class="abs quote" style="left:549px;top:1061px">”</div>

<footer class="abs footer"></footer>
<div class="abs badge" style="left:88px"></div>
<div class="abs badge" style="left:132px;background:#b9a23c"></div>
<div class="abs" style="left:180px;top:1112px;width:32px;height:36px;background:#c9643a"></div>
<div class="abs newsletter">NewsLetter :</div>
<div class="abs" style="left:306px;top:1118px;width:1px;height:22px;background:#777"></div>
<p class="abs nl-text">In venenatis neque a eros laoreet eu placerat erat suscipit.<br>Fusce cursus, erat et scelerisque condimentum</p>
<div class="abs nl-field">Enter Your Email Address :</div>
<svg class="abs" style="left:490px;top:1130px" width="12" height="8" viewBox="0 0 12 8"><rect x=".5" y=".5" width="11" height="7" fill="none" stroke="#999"/><path d="M.5 .5 L6 4.5 L11.5 .5" fill="none" stroke="#999"/></svg>
<svg class="abs" style="left:620px;top:1129px" width="6" height="9" viewBox="0 0 6 9"><path d="M1 1 L5 4.5 L1 8" stroke="#999" fill="none"/></svg>
<div class="abs foot-rule"></div>
<p class="abs copy">© Copy Rights 2014 Summit Path Advisory.All Rights Reserved</p>
<div class="abs social" style="left:525px"></div>
<div class="abs social" style="left:551px"></div>
<div class="abs social" style="left:576px"></div>
<div class="abs social" style="left:601px"></div>
<div class="abs social" style="left:626px"></div>
</body>
</html>
```